Web Design Project

To Create new charity website currently (www.morvalenhope.org)
Please request for full requirements in PDF format via email.
dilan.perow@morvalenhope.org cc: dperow_dp@quillmail.com.au

Im unable to load the project details on this page through add files feature. Please ensure you understand the requirments and use www.brightkinfold.com as a good reference. or guide.

Create Users , Registers a Child for Sponsor, Search for a Child to sponsor byCountry, Town, Age group, Gender, Race, Religion days waiting

Donate, Shop from MHG Store, Events, what we do, Get Involved Category, gallery, Upcoming events.

-Main Focus on Child Sponsor
Online Registeration request for Child Support to MHG Team allow document upload by the registering person.

MHG Team reviews the request checking and verifying all the details including documents submitted
(this will be published after being approved by MHG Committee. once approved then MHG Publishes the details for sponsors

There should be section where highlights are uniquely identified. such as upcoming event or shows, Appeal for Cyclone or Flood Relief or Medical Assistance.
May be scrolling text or something similar.
#Manage community fundraisers and display their information, performance etc. Automated online letter on thanks, support and reminders such as Bdays and payment renewals.

#The addition should consist of online database which tracks upcoming fundraising events, fundraisers, team and donations. Photo and events gallery. Sponsors,
Online ecards, registerations of sponsor, members, volunteers and all internet users who want to receive regular updates.

Registeration database to create users by category (may be)
sponsor, looking for sponsors, volunteers, members, donors, others etc. create registeration and capture info in database
name , dob, gender, country, email add, phone
registeration needs to be verified by email confirmation link send back to email add supplied for verification

1. A fundraising home page with an attractive layout that displays an overview of fundraising events, teams and individuals. This information could be organized by event location, date etc.

2. Event Home page for each fundraising event. We need to tap into our e-commerse setup to allow us to include a) a gauge of how much has been raised so far, b) a list of recent donors and their messages c) a way for people to donate directly to the fundraiser or team member, and d) some sort of blog that the fundraiser themselves can update with pictures and information.

admin page.
number of visits made to web site.
registered members
After its launched it wil be manages by our members,

reference to www.brightkinfold.com/ our members have liked this very much
and also get involved from and shop from http://tarwickaid.org.au/ to get more ideas and use only as a reference to bring user friendliness and efficient elegant look and ease of use to users.

The final product modern and inspire people to get involved and fundraise. and provide online donations and gifts and also shopping benefits through our web site to get discounts to all internet shoppers

Administration Page.

////////////////////////////////////////////////////////////////////////////////////////////
Registeration is required for
for sponsors, Child looking for sponsor, Shopping Donors, Members Volunteers etc

Username / Password
User details name
Name (s) First, Last Middle Address, Suburb/Town, Country, Post Code, +
Land Line: Country Code/Area Code/#
Mobile: Country Code/Number
Password Reset Method via email or secret Q/A at least 2.

Other functions as a registered users of MHG to provide
Account Summary
My Sponsorship
Additional Givings
Write my Child/Sponsor
make a Payment
Account Settings
Payment Options
My Activity
Questions.

I need the Unique identifyiny feature for upcoming event appeal for something that attracts peoples attention.

May be a bold scrolling text such : Morvalen Hope Group has lauched KORALI STORM DRIVE 2013, or Priyanka Medical Assistance Appeal and once a person clicks on the scrolling text get the full details of the appeal and what needs to be done to support. Should not be limited to only 1 appeal but may be upto 512 Characters or some better ways of presenting. eg may be there is appeal, fund raiser, medical assistance etc.

Childs Sponsor and other activity
Register a Child
Search for a Child
Sponsor a Child

Persons willing to register for a chile Online Registration request for Child Support

Name, middle Surname,
Age: 9 (calculated Automatically from DOB)
• Birthday: February 15, 2004 (Drop Down Box_
• Gender: Female (Radio button)
• Country: (select from List)
• Town/City: (select from List)
• Suburb/Village: (User Entry If Doesn’t Exist) Or better approach
• Ethnicity/Race: (User Enter if doesn’t exist) Or better approach
• Religion: (User Enters If doesn’t exist) Or better approach
• Photo
• Child ID: Automatically Generated by System
o Initial Registeration Child ID will be prefixed by letter z. eg z123456
o Once approved and published by MHG Administrator prefix z will be removed. Automatically
MHG Administrator should be able to edit update add or delete any information from maintenance Page or from the database.

o Calculate from date of publishing Child Waiting: 257 Days for a sponsor
o
• Allow Upload of supporting document Document (Any Format for verification)
• Allow upload of Photos (s) max of 3

Registeration MUST
All Person who are looking for Child to support or looking for sponsors or donations charity membership, Volunteers subscribing for new letters and events must register first, Social networking.

TO Register with MHG
Username, password min of 6 max 10, Firstname, Lastname, TownCity, Country, email:
Optional:
Phone: country code, area code number Mobile: Country Code, Mobile number
Every registered person should be able to see all HIS ACTIVITY donations and other details under his profile:

Administration Page
Easy Manageable Admin Page
All step by step guide of updating each and every page
Tools and software must be provided for managing the website.
Easy and efficient way of Managing Pictures Allow single multiple and all images in a folder to be uploaded in simple steps: Able to reset password if required.

Well Structured layout and defined layers links to each and every page. Home button to be available in all pages.

Reports
MHG Admin should be able to generate reports from database such as mysql if any other db used some simple queries or adhoc report to be generated
Eg: All sales in MHG Store by date cateogy amount total sales by country and town grouped by:

Upcoming Events
Allows easy and user friendly interface for updating the pages for upcoming events.
MHG Admin should be able to send email to all registered users with attachments such as news letters, request for support etc etc

Gallery
MHG Admin should be able to able select the default folder to use for Scrolling images
Eg: 1 week I would all sponsored childs folder to be used to scroll all images
2nd week I may default to all events pics
3rd I may select Diaster relief
Or I can use random pics from all folders under gallery
My folder structure for gallery may be like this. I will select where Im uploading photos and then

Gallery
Childs
Disaster
Events
Stores (Note Stores will also have scrolling images for all items listed for sale) and it has to have a tag and stock list or number of items available once it reaches 0 it should be labeled out of stock.

• Create Child ID Automatically and Photos to MHG Team allow document upload by the registering person.

manage community fundraisers and display their information, performance etc. Automated online letter of thanks, support and reminders payment renewals due day and 7 days before due date. Bdays

Additional info that may be useful but not necessary and if it can improve in way to make our web site more attractive and efficient.
During Registeration needs to be verified by email confirmation link send back to email add supplied for verification and the user gets registered

2. Events page for each category fundraising team event.
Sponsor a Child
Micro Enterprise
Social Events
Medical Assitance
Relief & Assistance
IT Projects
Special Projects

We need to tap into our e-commerse setup to allow us to include
a) a gauge of how much has been raised so far, b) a list of recent donors and their messages c) a way for people to donate directly to the fundraiser or team member, and d) some sort of blog that the MHG fundraiser Team Leader themselves can update with pictures and information.

Number of visits made to web site.
Marketing links/ Ads

Example: http://www.brightkinfold.com/
our members have liked this very much
and also
get involved from and shop from
http://tarwickaid.org.au/

Updates

Hi All

I need to complete this project asap. may be in next 4 to 6 weeks maximum

so please submit you design overview, features functionality

thanks

Dilan

                                       

Project Details/Requirements

To Create new charity website currently (www.morvalenhope.org) reference www.brightkinfold.com

 

Create login (for sponsors, Child looking for sponsor, Shopping Donors, Members Volunteers etc

               Username / Password

               User details name

                              Name (s) First, Last Middle Address, Suburb/Town, Country, Post Code,  +

 

Other functions as a registered users of MHG  to provide

Account Summary

My Sponsorship

Additional Givings

Write my Child/Sponsor

make a Payment

Account Settings

Payment Options

My Activity

Questions.

 

Reference to snapshot below

 

 

 

 

 

Change the background colour. Need to have a good search feature for the child. Refer to www.brightkinfold.org web site as a guide pretty much very similar features I need. Also

 

 

               Register a Child

               Search for a Child

               Sponsor a Child

 

 

<!-[if !supportLists]->·        <!-[endif]->Online Registration request for Child Support

<!-[if !supportLists]->·        <!-[endif]->Age: 9  (calculated Automatically from DOB)

<!-[if !supportLists]->·        <!-[endif]->Birthday: February 15, 2004  (Drop Down Box_

<!-[if !supportLists]->·        <!-[endif]->Gender: Female (Radio button)

<!-[if !supportLists]->·        <!-[endif]->Country: (select from List)

<!-[if !supportLists]->·        <!-[endif]->Town/City: (select from List)

<!-[if !supportLists]->·        <!-[endif]->Suburb/Village: (User Entry If Doesn’t Exist) Or better approach

<!-[if !supportLists]->·        <!-[endif]->Ethnicity/Race: (User Enter if doesn’t exist) Or better approach

<!-[if !supportLists]->·        <!-[endif]->Religion: (User Enters If doesn’t exist) Or better approach

<!-[if !supportLists]->·        <!-[endif]->Photo

<!-[if !supportLists]->·        <!-[endif]->Child ID: Automatically Generated by System

<!-[if !supportLists]->o   <!-[endif]->Initial Registeration Child ID will be prefixed by letter z. eg z123456

<!-[if !supportLists]->o   <!-[endif]->Once approved and published by MHG Administrator prefix z will be removed. Automatically

<!-[if !supportLists]->·        <!-[endif]-> 

<!-[if !supportLists]->o   <!-[endif]->Calculate from date of publishing Child Waiting: 257 Days for a sponsor

<!-[if !supportLists]->o   <!-[endif]-> 

<!-[if !supportLists]->·        <!-[endif]->Allow Upload of supporting document Document (Any Format for verification)

<!-[if !supportLists]->·        <!-[endif]->Allow upload of Photos (s) max of 3

 

Registeration MUST

 

TO Register with MHG

Optional:

Phone: country code, area code number  Mobile: Country Code, Mobile number

 

 

 

            

                           

Administration Page

Easy and efficient way of Managing Pictures Allow single multiple and all images in a folder to be uploaded in simple steps

 

              

Reports

 

Upcoming Events

 

Gallery

 

               Gallery

                              Childs

                              Disaster

                              Events

                              Stores  (Note Stores will also have scrolling images for all items listed for sale) and it has to have a tag and stock list or number of items available once it reaches 0 it should be labeled out of stock.

                             

 

 

<!-[if !supportLists]->·        <!-[endif]->Create Child ID Automatically and Photos  to MHG Team allow document    upload by the registering person.

<!-[if !vml]-><!-[endif]->

         MHG Team reviews the request checking and verifying all the details including    documents submitted

        

        

manage community fundraisers and display their information, performance etc. Automated online letter of thanks, support and reminders payment renewals due day and 7 days before due date.  Bdays

 

 

 

Sponsor a Child

                              Micro Enterprise

                              Social Events

                              Medical Assitance

                              Relief & Assistance

                              IT Projects

                              Special Projects

 

                             

 

Marketing links/ Ads

 

 

 

 

and also

http://tarwickaid.org.au/

 

 

 

 

                                   

Target Market(s)

get and attract as many charity supporters as possible

Industry/Entity Type

Internet

Requirements
Must have
• Refer to attached documents
Users manual or step by step guide on how to manage and update web pages.
Nice to have
• nice catchy looks and layout
Reporting online options

```html
<!DOCTYPE html>
<html lang="en">
<head>
<meta charset="utf-8">
<title>Morvalen Hope Australia — Sponsor a Child</title>
<link rel="stylesheet" href="https://fonts.googleapis.com/css2?family=PT+Sans:wght@400;700&family=Oswald:wght@500;700&family=Arimo:wght@400;700&family=Crimson+Text:ital@1&display=swap">
<style>
:root{
  --sky:#e9eef2;
  --olive:#a8b34d;
  --olive-dark:#8e9a3a;
  --brand-blue:#1b7fc4;
  --brand-blue-dark:#0f5fa3;
  --panel-blue:#1a93d6;
  --button-blue:#0e58b8;
  --lime:#b4c934;
  --lime-dark:#3f5a12;
  --ink:#333;
  --muted:#666;
  --card-grey:#e4e4e4;
  --menu-dark:#474747;
  --footer-band:#d6d6d6;
  --footer-dark:#484848;
  --footer-link:#b3bd4f;
  --white:#fff;
}
*{box-sizing:border-box;margin:0;padding:0}
html,body{width:814px;height:1200px;overflow:hidden}
body{position:relative;font-family:"PT Sans",sans-serif;color:var(--ink);
  background:linear-gradient(180deg,#f4f6f8 0,#dfe5ea 240px,#c9cfa0 380px,var(--olive) 470px,var(--olive) 1028px)}
.abs{position:absolute}
.scenery{left:0;top:0;width:814px;height:500px;
  background:radial-gradient(ellipse 260px 200px at 700px 120px,rgba(60,60,55,.45),transparent 70%),
             radial-gradient(ellipse 200px 160px at 60px 330px,rgba(80,90,60,.35),transparent 70%)}
.site-search{left:296px;top:13px;width:254px;height:22px;background:var(--white);border:1px solid #c8c8c8;
  font:11px "Arimo",sans-serif;color:#888;padding:4px 8px}
.site-search svg{position:absolute;right:6px;top:4px}
.brand{left:63px;top:50px;display:flex;align-items:center;gap:8px}
.brand-mark{width:26px;height:26px;border-radius:50%;background:var(--panel-blue)}
.brand-name{font:700 21px "PT Sans",sans-serif;color:var(--panel-blue);letter-spacing:.5px;line-height:1}
.brand-sub{left:97px;top:76px;font:400 9px "PT Sans",sans-serif;letter-spacing:9px;color:#555}
.donate{left:548px;top:62px;width:176px;height:92px;background:var(--lime);transform:rotate(-4deg);text-align:center;padding-top:14px}
.donate-title{font:700 28px "PT Sans",sans-serif;color:#333;line-height:1}
.donate-btn{display:inline-block;margin-top:8px;background:var(--lime-dark);color:#d9ef5c;font:700 10px "PT Sans",sans-serif;padding:3px 14px;border-radius:3px}
.main-nav{left:70px;top:141px;width:435px;height:32px;border-radius:4px;background:linear-gradient(var(--brand-blue),var(--brand-blue-dark));
  display:flex;align-items:center;padding-left:10px}
.main-nav a{color:var(--white);text-decoration:none;font:400 11px "Arimo",sans-serif;padding:0 7px;border-right:1px solid rgba(255,255,255,.55);line-height:14px}
.main-nav a:last-child{border:0}
.content{left:70px;top:182px;width:435px;height:816px;background:var(--white)}
.slider{left:7px;top:8px;width:420px;height:179px;background:linear-gradient(135deg,#6a5a3c,#a89070 45%,#d8d2c4 70%,#4e6b46)}
.slider-caption{position:absolute;left:0;top:60px;width:420px;height:70px;background:rgba(255,255,255,.28);
  font:italic 21px "Crimson Text",serif;color:var(--white);padding:10px 0 0 25px;line-height:26px}
.slider-caption span{display:block;padding-left:200px}
.slider-dots{position:absolute;left:10px;top:152px;display:flex;gap:5px}
.slider-dots i{width:8px;height:8px;border-radius:50%;background:var(--white)}
.slider-dots i:first-child{background:var(--panel-blue);box-shadow:0 0 0 1px #fff}
.section-title{font:700 21px "PT Sans",sans-serif;color:var(--brand-blue-dark)}
.section-title.small{font:400 14px "PT Sans",sans-serif;color:var(--panel-blue)}
.child-card{top:250px;width:124px;height:172px;background:var(--card-grey);padding:7px;text-align:center}
.child-photo{width:110px;height:107px;background:linear-gradient(160deg,#c9b79a,#7e5b43 60%,#e8e4dc)}
.child-name{font:700 10px "Arimo",sans-serif;color:var(--brand-blue-dark);margin-top:6px;padding-bottom:3px;border-bottom:1px solid #c9cf98}
.child-meta{font:400 10px "Arimo",sans-serif;color:var(--muted);margin-top:3px;line-height:13px}
.sponsor-btn{top:426px;width:124px;height:20px;border-radius:3px;background:linear-gradient(#2a78d6,var(--button-blue));
  color:var(--white);font:700 11px "Arimo",sans-serif;text-align:center;line-height:20px}
.info-box{left:10px;top:458px;width:415px;height:67px;background:var(--card-grey);padding:12px 13px;
  font:400 9.5px "Arimo",sans-serif;color:#7a7a7a;line-height:11.5px}
.info-btn{position:absolute;right:9px;bottom:7px;width:117px;height:20px;border-radius:3px;background:linear-gradient(#2a78d6,var(--button-blue));
  color:var(--white);font:700 10.5px "Arimo",sans-serif;text-align:center;line-height:20px}
.appeal{left:10px;top:542px;width:415px;height:137px;background:linear-gradient(110deg,#5a4a2f,#8b7c5c 50%,#b5ad97);overflow:hidden}
.appeal-title{position:absolute;left:25px;top:12px;font:700 34px/38px "Oswald",sans-serif;color:#e8b41e;text-transform:uppercase}
.appeal-title small{font-size:20px}
.appeal-note{position:absolute;left:130px;top:112px;width:190px;font:400 7px "Arimo",sans-serif;color:#eee;text-align:right;line-height:9px}
.appeal-btn{position:absolute;left:343px;top:109px;width:66px;height:20px;background:#f1b21e;font:700 7.5px/20px "Arimo",sans-serif;color:#333;text-align:center}
.press-strip{left:10px;top:727px;width:415px;height:67px;border:1px solid #d8d8d8;display:flex;justify-content:space-around;align-items:center}
.press-strip i{display:block;width:56px;height:16px;background:#cfcfcf;border-radius:2px}
.child-search{left:520px;top:182px;width:222px;height:242px;background:var(--panel-blue);padding:12px 19px;color:var(--white)}
.child-search h2{font:400 21px "PT Sans",sans-serif;margin-bottom:4px}
.child-search label{display:block;font:700 10px "PT Sans",sans-serif;margin-top:10px}
.select{margin-top:3px;height:25px;background:var(--white);border:1px solid #bcd;color:#222;font:400 10.5px "Arimo",sans-serif;padding:5px 4px;position:relative}
.select::after{content:"";position:absolute;right:3px;top:4px;width:14px;height:14px;background:#d8e4f2;border:1px solid #9ab}
.range{margin-top:10px;height:8px;background:#ddd;border-radius:3px;position:relative}
.range i{position:absolute;top:-3px;width:7px;height:13px;background:#bbb;border:1px solid #999}
.search-btn{margin-top:20px;width:81px;height:21px;border-radius:3px;background:linear-gradient(#2a78d6,var(--button-blue));font:700 10.5px/21px "Arimo",sans-serif;text-align:center}
.sidebar{left:520px;top:446px;width:222px;height:552px;background:var(--white)}
.side-link{left:9px;width:205px;height:37px;background:var(--menu-dark);color:var(--white);font:400 13px/31px "PT Sans",sans-serif;padding-left:22px}
.side-link::before{content:"";position:absolute;left:10px;top:14px;width:4px;height:4px;border-radius:50%;background:var(--white)}
.side-link.active{color:#f2d52b;text-decoration:underline}
.side-link.active::before{background:#f2d52b}
.promo{left:9px;top:196px;width:206px;height:334px;background:linear-gradient(180deg,#1c86c4,#0f6ea8);overflow:hidden}
.promo-photo{position:absolute;left:0;top:40px;width:100px;height:294px;background:linear-gradient(180deg,#7a5548,#e04f9a 45%,#c13e86)}
.promo-badge{position:absolute;left:106px;top:2px;width:106px;height:106px;border-radius:50%;border:2px solid #3ba5e0;
  font:500 19px/20px "Oswald",sans-serif;color:#9fd8f5;text-align:center;padding-top:24px}
.promo-badge span{color:#c2e6f8;font-size:16px}
.promo-head{position:absolute;left:86px;top:112px;width:120px;text-align:center;font:700 16px/18px "Oswald",sans-serif;color:var(--white)}
.promo-sub{position:absolute;left:96px;top:220px;width:104px;text-align:center;font:500 13px/16px "Oswald",sans-serif;color:#f1b21e}
.promo-btn{position:absolute;left:73px;top:280px;width:122px;height:35px;border-radius:3px;background:linear-gradient(#f5c43a,#e79a10);
  font:700 15px/35px "Arimo",sans-serif;color:#5a2f00;text-align:center}
.util-bar{left:0;top:1028px;width:814px;height:39px;background:var(--footer-band)}
.util-links{position:absolute;left:90px;top:13px;display:flex;gap:14px;font:400 11px "Arimo",sans-serif;color:#555}
.util-links a{color:#555;text-decoration:underline;display:flex;align-items:center;gap:5px}
.util-links svg{flex:none}
.social{position:absolute;left:564px;top:9px;display:flex;gap:9px}
.social i{display:block;width:21px;height:21px}
.footer{left:0;top:1067px;width:814px;height:133px;background:var(--footer-dark)}
.footer-col{top:14px;font:400 9.5px/15.5px "Arimo",sans-serif;color:var(--footer-link)}
.footer-bottom{left:73px;top:114px;width:662px;display:flex;justify-content:space-between;font:400 9.5px "Arimo",sans-serif;color:#ddd}
</style>
</head>
<body>
<div class="abs scenery" role="img" aria-label="Soft landscape backdrop with a large tree and green hills"></div>

<div class="abs site-search">Search
  <svg width="13" height="13" viewBox="0 0 13 13"><circle cx="7.5" cy="5.5" r="4" fill="none" stroke="#333" stroke-width="1.5"/><line x1="4.6" y1="8.4" x2="1" y2="12" stroke="#333" stroke-width="2"/></svg>
</div>

<div class="abs brand"><span class="brand-mark"></span><span class="brand-name">MORVALEN HOPE</span></div>
<div class="abs brand-sub">AUSTRALIA</div>

<div class="abs donate"><div class="donate-title">Donate Now</div><span class="donate-btn">Click Here</span></div>

<nav class="abs main-nav">
  <a>Home</a><a>About Us</a><a>Where We Work</a><a>Children &amp; Poverty</a><a>Get Involved</a><a>Blog</a>
</nav>

<main class="abs content">
  <div class="abs slider" role="img" aria-label="Photo of smiling schoolchildren in Fiji">
    <div class="slider-caption">Assisting the poor and needy<span>of Fiji since 2000...</span></div>
    <div class="slider-dots"><i></i><i></i><i></i></div>
  </div>

  <h1 class="abs section-title" style="left:16px;top:204px">Sponsor a Child Today</h1>

  <div class="abs child-card" style="left:18px"><div class="child-photo" role="img" aria-label="Photo of a child awaiting sponsorship"></div><div class="child-name">Tevita</div><div class="child-meta">Bangladesh<br>5/15/2005</div></div>
  <div class="abs child-card" style="left:155px"><div class="child-photo" role="img" aria-label="Photo of a child awaiting sponsorship"></div><div class="child-name">Tevita</div><div class="child-meta">Bangladesh<br>5/15/2005</div></div>
  <div class="abs child-card" style="left:294px"><div class="child-photo" role="img" aria-label="Photo of a child awaiting sponsorship"></div><div class="child-name">Tevita</div><div class="child-meta">Bangladesh<br>5/15/2005</div></div>
  <div class="abs sponsor-btn" style="left:18px">Sponsor</div>
  <div class="abs sponsor-btn" style="left:155px">Sponsor</div>
  <div class="abs sponsor-btn" style="left:294px">Sponsor</div>

  <div class="abs info-box">When you sponsor a child in poverty, your sponsored child will be linked directly to you. Your sponsored child will know your name and you will be able to write letters to each other.
    <div class="info-btn">View More Children</div>
  </div>

  <div class="abs appeal" role="img" aria-label="Photo of floodwater around a fence in the Philippines">
    <div class="appeal-title">Monsoon <small>hits</small><br><small>the</small>Philippines</div>
    <div class="appeal-note">More than 2.4 million people have been affected by the flooding in the Philippines. You can help bring immediate relief.</div>
    <div class="appeal-btn">Donate Now ›</div>
  </div>

  <h2 class="abs section-title small" style="left:12px;top:703px">Sponsor a Child Today</h2>
  <div class="abs press-strip"><i></i><i></i><i></i><i></i><i></i></div>
</main>

<aside class="abs child-search">
  <h2>Search for a Child</h2>
  <label style="margin-top:0">Where in the World</label>
  <div class="select">No Preference</div>
  <label style="margin-top:20px">Gender</label>
  <div class="select">No Preference</div>
  <label style="margin-top:20px">Age Range 3 to 22</label>
  <div class="range"><i style="left:13px"></i><i style="left:170px"></i></div>
  <div class="search-btn">Search Now</div>
</aside>

<aside class="abs sidebar">
  <div class="abs side-link active" style="top:11px">Sponsor a Child</div>
  <div class="abs side-link" style="top:55px">Rescue Babies &amp; Mothers</div>
  <div class="abs side-link" style="top:99px">Develop a Future Leader</div>
  <div class="abs side-link" style="top:144px">Meet Critical Needs</div>
  <div class="abs promo">
    <div class="promo-photo" role="img" aria-label="Photo of a young girl in a pink shirt"></div>
    <div class="promo-badge">CHANGE<br>THE STORY<br><span>THIS FALL</span></div>
    <div class="promo-head">GIVE A BRIGHTKINFOLD SUNDAY PRESENTATION THIS FALL</div>
    <div class="promo-sub">Speak from your heart and inspire others to sponsor</div>
    <div class="promo-btn">Learn more ›</div>
  </div>
</aside>

<div class="abs util-bar">
  <div class="util-links">
    <a><svg width="14" height="10" viewBox="0 0 14 10"><rect x=".5" y=".5" width="13" height="9" fill="#fff" stroke="#888"/><path d="M.5 .5 7 6 13.5 .5" fill="none" stroke="#888"/></svg>Email a Friend</a>
    <a><svg width="10" height="10" viewBox="0 0 10 10"><circle cx="1.5" cy="8.5" r="1.5" fill="#888"/><path d="M0 4a6 6 0 0 1 6 6M0 0a10 10 0 0 1 10 10" fill="none" stroke="#888" stroke-width="1.5"/></svg>Subscribe</a>
    <a><svg width="11" height="11" viewBox="0 0 11 11"><circle cx="2" cy="5.5" r="2" fill="#888"/><circle cx="9" cy="2" r="2" fill="#888"/><circle cx="9" cy="9" r="2" fill="#888"/><path d="M2 5.5 9 2M2 5.5 9 9" stroke="#888"/></svg>Bookmark &amp; Share</a>
    <a><svg width="12" height="11" viewBox="0 0 12 11"><rect x="3" y="0" width="6" height="4" fill="#fff" stroke="#888"/><rect x="0" y="4" width="12" height="5" fill="#888"/><rect x="3" y="7" width="6" height="4" fill="#fff" stroke="#888"/></svg>Print This Page</a>
  </div>
  <div class="social">
    <i style="background:#3b5998"></i><i style="background:#c8232c"></i><i style="background:#1da1f2"></i><i style="background:#1b6fc0"></i><i style="background:#d8261e"></i>
  </div>
</div>

<footer class="abs footer">
  <div class="abs footer-col" style="left:73px">Sponsor a Child<br>Rescue Babies &amp; Mothers<br>Develop a Future Leader<br>Meet Critical Needs<br>Donate Now<br>Home</div>
  <div class="abs footer-col" style="left:229px">Employment Opportunities<br>Press Center<br>Contact Us</div>
  <div class="abs footer-col" style="left:370px">Get Involved<br>Children &amp; Poverty<br>About Us</div>
  <div class="abs footer-col" style="left:491px">Blog<br>Brightkinfold Store<br>My Account<br>Support Network</div>
  <div class="abs footer-col" style="left:614px">Brightkinfold FAQ<br>New Brightkinfold.com FAQ<br>Site Map</div>
  <div class="abs footer-bottom"><span>© 2000, 2002-2012 Brightkinfold International. All Rights Reserved</span><span>Powered by: Nordvane Technologies</span></div>
</footer>
</body>
</html>
```